Dune Circle UAE - Website for Club Members

Dune Circle UAE Website

A simple but amazing website is needed for an offroad club in the UAE.

Dunecircle.ae (domain owned)
Hosting required.

Dune Circle UAE is a non-profit club that brings together Kovo owners who meet up and drive & gather together all over the country.

The club until now has been working on WhatsApp but has grown to over 700+ members and needs a website to support it and have a platform to book/sign up for trips. As there are many types of driving levels, we need a platform to categorise each member according to their driving skill so they can only signup for the trip that is in accordance with their level.

The page must be intuitive, easy and clean. We have many members from many different countries & ages. Keeping it simple would be good.
English is the main language. (Maybe an easy Google translation addon for Arabic)

Mobile friendly / web app:
Most of our members will use the page on their mobile, and admins will usually use the site on their mobiles to see who is on the trip, show reports, blog etc.

1. Member profile creation
● Login
● Sign up
● Recover password
• (Terms & Conditions Button) Captcha

2. Member Area
● Dynamic ranking (Admins to set levels)
• Master Admin (Master Access)
• Admins (Full Access)
• Management (Edit Options)
• Marshalls (Can Post Trips & add post-trip report)

● Member Level
• Trail (Beginner)
• Mesa (Intermediate)
• Falcon (Advanced)
• Warden (Expert)
• 517 (Teacher)
● Profile (Vehicle & Member info)

3. Member trip/events sign-ups
• Members can only see trips according to their tier
• (Example) Only Trail Should see Trips for “Trail Level” / Mesa can see Mesa Trips & Trail Trips / Falcon can see Falcon, Mesa & Trail Trips etc. Tiers can only see their level and below.
● A page with the list of trips (group by date)
● Sign up/out button
● The trip will contain:
○ Title
○ Picture
○ Description
○ Time and Location
○ Level limit
○ Trip creator/owner
○ Trip capacity limit
● Admin: add/remove members from trip
● Admin can create/manage trips
● Admin can rate (1 rating 1 to 5 stars) members in the trip

4. Sponsors Pages/s (tesk4x4, vol)
• Ability to add full pages according to the sponsorship level.
• Speciality Index (Fabrication, Mechanic, Wheel, Rims, painting)
● Ad area with Title, image, a short description and link

5. Dune Circle profile
• About Us page
• Rules and regulations, T&C’s.
• Roles
• Founders/Management area.

6, Blog Area.
• General blog, nothing complicated
• For example, an area where members can sell their used items, an area where they can chit-chat about new models etc.
• Only Admins can create posts/subjects.
• Blogs post should also be seen as per Member Level

7, Social media area.
● Simple place where we share our social media. @dunecircle.ae
• We only use Instagram for now but we will push Tik Tok soon.

8, E-Commerce
• Not a must at this moment but will be required in the future (1 year). Please account for this so we can activate it when required. Simple and easy.

9, Backend

• Backend Should be straightforward to use and intuitive, adding images/text, editing images/text, creating text (Font, size, colour), and adding pages. (For simple people to use one site). We do not require website management, but we will contact the developer if we need any big add-ons or want to expand the site.
• Mobile view is essential.
o We will use the website as a Web App for mobile devices. Mobile versions should be accessible, mobile like and intuitive.
• plain wallet tiles Membership Card option required. Members will be able to download their membership cards. (Simple, no picture) members details

Website References:
Dunecircle.ae (old website)
QP4x4
Lumen 4x4
UAE Trailhounds
Bravely 4x4

Target Market(s)

Club members & future club members

Industry/Entity Type

Offroad club

Coding

Coded - Design and coding required

Number of Pages Required

5+ page

Font styles to use
Other font styles liked:
• Helvetica

Colors
0054AA
0677BA
7BADD7
CADEEF
E8F1F8
EB3D1F
EC4F4E
F09395
F8D3D4
FCEDEE

Requirements
Must have
• Member/Profile Area, Member Level, Trips/Events area, Sponsors, Profile, Blog, E-commerce, easy & intuative backend.
Nice to have
• Simple, clean, attaractive, modern. Apple Wallet & Google Wallet option for memebers to downalod their mebership cards.
Should not have
• A very complicated backend.

```html
<!DOCTYPE html>
<html lang="en">
<head>
<meta charset="utf-8">
<title>Dune Circle UAE</title>
<link href="https://fonts.googleapis.com/css2?family=Inter:wght@400;500;600;700;800&display=swap" rel="stylesheet">
<style>
:root{
  --red:#d7323a;
  --ink:#1d1d1f;
  --muted:#555;
  --soft:#9a9a9a;
  --panel:#f2f2f2;
  --line:#dcdcdc;
  --dark:#2c2c2c;
  --navy:#1b2436;
  --online:#22c42c;
}
*{margin:0;padding:0;box-sizing:border-box}
html,body{width:1200px;height:3409px;overflow:hidden;background:#fff}
body{position:relative;font-family:"Inter",Helvetica,Arial,sans-serif;color:var(--ink)}
.abs{position:absolute}
a{color:inherit;text-decoration:none}

/* header */
.brand{left:104px;top:52px;font-weight:800;font-size:26px;color:var(--red);letter-spacing:.5px;display:flex;align-items:center;gap:8px}
.brand i{width:16px;height:16px;border-radius:50%;background:var(--red);display:block}
.member-link{top:31px;display:flex;align-items:center;gap:8px;font-size:13px;color:#333}
.member-link span.ic{width:26px;height:26px;border-radius:50%;background:var(--red);display:flex;align-items:center;justify-content:center}
.pill{top:29px;height:32px;border-radius:16px;background:var(--red);color:#fff;font-weight:700;font-size:14px;display:flex;align-items:center;justify-content:center}
.navbar{left:0;top:86px;width:1200px;height:53px}
.nav-item{top:103px;color:#fff;font-weight:700;font-size:13.5px}

/* hero */
.hero{left:0;top:139px;width:1200px;height:559px;background:linear-gradient(180deg,#5d9ed6 0%,#9cc4e4 28%,#d9b48a 48%,#c98a4e 70%,#b8733c 100%)}
.hero h1{position:absolute;left:0;width:1200px;top:55px;text-align:center;color:#fff;font-weight:800;font-size:52px;line-height:58px;text-shadow:0 2px 6px rgba(0,0,0,.45)}
.btn-red{background:var(--red);color:#fff;font-weight:700;border-radius:26px;display:flex;align-items:center;justify-content:center}

/* sections */
.section-title{font-weight:800;font-size:40px;letter-spacing:.3px;color:var(--ink)}
.photo{border-radius:0}
.about-text{left:445px;top:849px;width:290px;font-size:11.5px;line-height:17.5px;color:#333}
.about-text p{margin-bottom:17px}

.panel{background:var(--panel)}
.field{background:#fff;border-radius:22px;height:42px;font-size:11px;color:#333;padding-left:15px;display:flex;align-items:center}

.card{left:140px;width:589px;height:204px;border:1.5px solid var(--line);background:#fff}
.card .pic{position:absolute;left:19px;top:15px;width:208px;height:172px}
.card h3{position:absolute;left:260px;top:46px;width:320px;font-size:18.5px;line-height:22px;font-weight:700}
.meta{display:flex;gap:16px;font-size:13px;font-weight:700;color:#333;align-items:center}
.meta .by{color:var(--red)}
.meta span{display:flex;align-items:center;gap:5px}
.card .meta{position:absolute;left:263px;top:113px}
.tags{position:absolute;left:263px;top:149px;display:flex;gap:14px;font-size:10.5px;color:var(--soft)}

.side-title{font-weight:700;font-size:24px;color:#222}
.trip{left:799px;width:230px;font-size:13px;line-height:17px;color:#444}
.trip .meta{font-size:11.5px;gap:14px;margin-top:6px}
.trip .meta .loc{color:var(--red)}
.trip .meta .by{color:#333;font-weight:600}
.roles{left:800px;top:1788px;list-style:none;font-size:21px;color:#222}
.roles li{height:47px}
.roles li::before{content:"• ";font-size:16px}

.member{left:802px;display:flex;align-items:center;gap:14px}
.avatar{width:66px;height:66px;border-radius:50%;background:linear-gradient(135deg,#9fc0de,#5a6f86)}
.member b{font-size:13.5px;display:block;color:#222}
.member small{font-size:12.5px;color:var(--soft);font-weight:600;padding-left:3px}
.dot{width:13px;height:13px;border-radius:50%;background:var(--online)}

/* newsletter */
.newsletter{left:0;top:2882px;width:1200px;height:148px}
.news-title{left:150px;top:2933px;color:#fff;font-weight:700;font-size:32px}
.email{left:557px;top:2922px;width:347px;height:59px;background:#fff;border-radius:30px;font-size:12px;color:#bbb;padding-left:18px;display:flex;align-items:center}
.signup{left:913px;top:2922px;width:135px;height:59px;background:var(--navy);color:#fff;border-radius:30px;font-weight:700;font-size:16px;display:flex;align-items:center;justify-content:center}

/* footer */
.foot-brand{left:130px;top:3158px;font-weight:800;font-size:30px;color:var(--red);display:flex;align-items:center;gap:8px}
.foot-brand i{width:18px;height:18px;border-radius:50%;background:var(--red);display:block}
.foot-col h4{font-weight:600;font-size:21px;color:#4a4a4a;line-height:25px}
.foot-col ul{list-style:none;margin-top:12px}
.foot-col li{font-size:12px;color:#777;height:23.8px}
.tile{width:72px;height:71px;border-radius:12px}
.social{width:36px;height:36px;border-radius:50%;background:#1a1a2a}
.rule{left:150px;top:3334px;width:902px;height:1px;background:#e2e2e2}
.copy{left:0;width:1200px;top:3370px;text-align:center;font-size:13px;color:#555}
</style>
</head>
<body>

<!-- header -->
<div class="abs brand"><i></i>DUNE CIRCLE</div>

<div class="abs member-link" style="left:333px"><span class="ic"><svg width="14" height="14" viewBox="0 0 14 14"><circle cx="7" cy="4.5" r="3" fill="#fff"/><path d="M1.5 13c0-3.2 2.5-5 5.5-5s5.5 1.8 5.5 5z" fill="#fff"/></svg></span>Member profile</div>
<div class="abs member-link" style="left:486px"><span class="ic"><svg width="16" height="14" viewBox="0 0 16 14"><circle cx="5" cy="4.5" r="2.6" fill="#fff"/><circle cx="11" cy="4.5" r="2.6" fill="#fff"/><path d="M0.5 13c0-2.8 2-4.4 4.5-4.4S9.5 10.2 9.5 13zM6.5 13c0-2.8 2-4.4 4.5-4.4s4.5 1.6 4.5 4.4z" fill="#fff"/></svg></span>Member Area</div>
<div class="abs member-link" style="left:635px"><span class="ic"><svg width="14" height="14" viewBox="0 0 14 14"><circle cx="6" cy="4.5" r="3" fill="#fff"/><path d="M0.5 13c0-3.2 2.5-5 5.5-5 1.5 0 2.8.4 3.8 1.2L7.5 13z" fill="#fff"/><path d="M9 11l1.5 1.5L13.5 9" stroke="#fff" stroke-width="1.6" fill="none"/></svg></span>Member Level</div>
<div class="abs member-link" style="left:786px"><span class="ic"><svg width="15" height="14" viewBox="0 0 15 14"><circle cx="6" cy="4.5" r="3" fill="#fff"/><path d="M0.5 13c0-3.2 2.5-5 5.5-5s5.5 1.8 5.5 5z" fill="#fff"/><path d="M12 2v5M9.5 4.5h5" stroke="#fff" stroke-width="1.6"/></svg></span>Member trip</div>

<a class="abs pill" style="left:919px;width:76px">Log in</a>
<a class="abs pill" style="left:1002px;width:95px">Register</a>

<svg class="abs navbar" viewBox="0 0 1200 53" preserveAspectRatio="none">
  <rect x="0" y="49" width="300" height="4" fill="#111"/>
  <polygon points="298,0 1200,0 1200,53 258,53" fill="#000"/>
</svg>
<a class="abs nav-item" style="left:320px">Home</a>
<a class="abs nav-item" style="left:388px">About Dune Circle</a>
<a class="abs nav-item" style="left:552px">Forums</a>
<a class="abs nav-item" style="left:640px">Sponsors</a>
<a class="abs nav-item" style="left:741px">E-Commerce</a>
<a class="abs nav-item" style="left:868px">Blog</a>
<svg class="abs" style="left:1032px;top:102px" width="20" height="20" viewBox="0 0 20 20"><circle cx="8" cy="8" r="6" stroke="#fff" stroke-width="2.6" fill="none"/><path d="M12.5 12.5L18 18" stroke="#fff" stroke-width="3" stroke-linecap="round"/></svg>
<div class="abs" style="left:1066px;top:101px;width:20px;height:20px;border:2px solid #fff;border-radius:50%" role="img" aria-label="Social profile"></div>

<!-- hero -->
<section class="abs hero" role="img" aria-label="Photo of a club member with arms spread in front of a row of off-road vehicles on desert dunes under a cloudy blue sky">
  <h1>WANT TO BECOME<br>A DESERT EXPERT?</h1>
  <a class="abs btn-red" style="left:511px;top:180px;width:177px;height:49px;font-size:15px">BOOK FOR TRIPS</a>
</section>

<!-- about -->
<h2 class="abs section-title" style="left:150px;top:770px">ABOUT DUNE CIRCLE UAE</h2>
<div class="abs photo" style="left:151px;top:845px;width:263px;height:317px;background:linear-gradient(180deg,#7fb1e0 0%,#a7c8e6 35%,#d39a5c 60%,#c9844a 100%)" role="img" aria-label="Group photo of club members sitting in the sand in front of an off-road vehicle"></div>
<div class="abs about-text">
  <p>The Dune Circle UAE Club is made up of off-roading enthusiasts brought together by the love of their KOVO, one of the world’s greatest off-road motoring companies in the world.</p>
  <p>Since 2018 we’ve been driving through and around the UAE, organizing Wadi, Cross Country &amp; desert trips, social gatherings, desert training, exhibitions &amp; Car shows, inter-club meetings, coastal cleanups, breast cancer awareness meetings and much more.</p>
  <p>Whether you’re driving a KOVO that’s new or old, we’re all about the driving experience everyone and any one &nbsp;is welcome from the UAE</p>
</div>
<a class="abs btn-red" style="left:441px;top:1122px;width:120px;height:42px;font-size:13px">READ MORE</a>

<!-- login -->
<div class="abs panel" style="left:773px;top:851px;width:279px;height:317px"></div>
<div class="abs" style="left:773px;top:890px;width:279px;text-align:center;font-size:18px;font-weight:600"><span style="color:var(--red)">Login</span> &nbsp;•&nbsp; Register</div>
<div class="abs field" style="left:791px;top:931px;width:244px">Username:</div>
<div class="abs field" style="left:791px;top:987px;width:244px">Password:</div>
<div class="abs" style="left:800px;top:1047px;display:flex;align-items:center;gap:8px;font-size:12.5px;color:#444"><span style="width:13px;height:13px;border:1px solid #888;background:#fff;display:block"></span>Remember me</div>
<a class="abs btn-red" style="left:791px;top:1082px;width:244px;height:43px;font-size:12.5px">LOGIN</a>

<!-- recent events -->
<h2 class="abs section-title" style="left:150px;top:1233px">RECENT EVENTS</h2>

<div class="abs card" style="top:1306px">
  <div class="pic" style="background:linear-gradient(180deg,#8ab3d8,#b9c6cf 45%,#6d7378 100%)" role="img" aria-label="Grey off-road vehicle parked on a city street"></div>
  <h3>Kovo Officially Reveals the 2021 Production Strider Falcon 517!</h3>
  <div class="meta"><span><svg width="10" height="14" viewBox="0 0 10 14"><path d="M5 0a5 5 0 0 0-5 5c0 3.5 5 9 5 9s5-5.5 5-9a5 5 0 0 0-5-5zm0 7a2 2 0 1 1 0-4 2 2 0 0 1 0 4z" fill="#333"/></svg>UAE</span><span><svg width="12" height="12" viewBox="0 0 12 12"><rect x="0" y="2" width="12" height="10" fill="#333"/><rect x="2" y="0" width="2" height="3" fill="#333"/><rect x="8" y="0" width="2" height="3" fill="#333"/></svg>22.6.2023</span><span class="by"><svg width="12" height="12" viewBox="0 0 12 12"><circle cx="6" cy="3.5" r="3" fill="#d7323a"/><path d="M0 12c0-3.5 2.7-5 6-5s6 1.5 6 5z" fill="#d7323a"/></svg>by Tarek</span></div>
  <div class="tags"><span>Off-Road</span><span>Automotive</span><span>Club</span><span>Reviews</span></div>
</div>

<div class="abs card" style="top:1531px">
  <div class="pic" style="background:linear-gradient(160deg,#d7c08c,#c9a64a 50%,#8a6d30 100%)" role="img" aria-label="Yellow off-road vehicle among rocks"></div>
  <h3>Kovo Officially Reveals the 2021 Production Strider Falcon 517!</h3>
  <div class="meta"><span><svg width="10" height="14" viewBox="0 0 10 14"><path d="M5 0a5 5 0 0 0-5 5c0 3.5 5 9 5 9s5-5.5 5-9a5 5 0 0 0-5-5zm0 7a2 2 0 1 1 0-4 2 2 0 0 1 0 4z" fill="#333"/></svg>UAE</span><span><svg width="12" height="12" viewBox="0 0 12 12"><rect x="0" y="2" width="12" height="10" fill="#333"/><rect x="2" y="0" width="2" height="3" fill="#333"/><rect x="8" y="0" width="2" height="3" fill="#333"/></svg>22.6.2023</span><span class="by"><svg width="12" height="12" viewBox="0 0 12 12"><circle cx="6" cy="3.5" r="3" fill="#d7323a"/><path d="M0 12c0-3.5 2.7-5 6-5s6 1.5 6 5z" fill="#d7323a"/></svg>by Tarek</span></div>
  <div class="tags"><span>Off-Road</span><span>Automotive</span><span>Club</span><span>Reviews</span></div>
</div>

<div class="abs card" style="top:1756px">
  <div class="pic" style="background:linear-gradient(180deg,#e7a24e,#f0c98f 45%,#5f656c 70%,#d8c3a0 100%)" role="img" aria-label="Dark grey off-road vehicle on sand at sunset"></div>
  <h3>Kovo Officially Reveals the 2021 Production Strider Falcon 517!</h3>
  <div class="meta"><span><svg width="10" height="14" viewBox="0 0 10 14"><path d="M5 0a5 5 0 0 0-5 5c0 3.5 5 9 5 9s5-5.5 5-9a5 5 0 0 0-5-5zm0 7a2 2 0 1 1 0-4 2 2 0 0 1 0 4z" fill="#333"/></svg>UAE</span><span><svg width="12" height="12" viewBox="0 0 12 12"><rect x="0" y="2" width="12" height="10" fill="#333"/><rect x="2" y="0" width="2" height="3" fill="#333"/><rect x="8" y="0" width="2" height="3" fill="#333"/></svg>22.6.2023</span><span class="by"><svg width="12" height="12" viewBox="0 0 12 12"><circle cx="6" cy="3.5" r="3" fill="#d7323a"/><path d="M0 12c0-3.5 2.7-5 6-5s6 1.5 6 5z" fill="#d7323a"/></svg>by Tarek</span></div>
  <div class="tags"><span>Off-Road</span><span>Automotive</span><span>Club</span><span>Reviews</span></div>
</div>

<!-- upcoming trips -->
<div class="abs panel" style="left:773px;top:1214px;width:279px;height:450px"></div>
<h3 class="abs side-title" style="left:799px;top:1244px">UpcomingTrips</h3>
<div class="abs trip" style="top:1297px">Lorem ipsum dolor sit amensecte tipiscing elit, sed do eiuolor.<div class="meta"><span class="loc">⬤ UAE</span><span>▪ 22.6.2023</span><span class="by">by Tarek</span></div></div>
<div class="abs trip" style="top:1385px">Lorem ipsum dolor sit amensecte tipiscing elit, sed do eiuolor.<div class="meta"><span class="loc">⬤ UAE</span><span>▪ 22.6.2023</span><span class="by">by Tarek</span></div></div>
<div class="abs trip" style="top:1478px">Lorem ipsum dolor sit amensecte tipiscing elit, sed do eiuolor.<div class="meta"><span class="loc">⬤ UAE</span><span>▪ 22.6.2023</span><span class="by">by Tarek</span></div></div>
<div class="abs trip" style="top:1569px">Lorem ipsum dolor sit amensecte tipiscing elit, sed do eiuolor.<div class="meta"><span class="loc">⬤ UAE</span><span>▪ 22.6.2023</span><span class="by">by Tarek</span></div></div>

<!-- member area -->
<div class="abs panel" style="left:773px;top:1696px;width:279px;height:351px"></div>
<h3 class="abs side-title" style="left:800px;top:1734px">Member Area</h3>
<ul class="abs roles">
  <li>Dynamic ranking</li>
  <li>Master Admin</li>
  <li>Admins</li>
  <li>Management</li>
  <li>Marshalls</li>
</ul>

<!-- recent posts -->
<h2 class="abs section-title" style="left:150px;top:2047px">RECENT POSTS</h2>

<div class="abs card" style="top:2119px">
  <div class="pic" style="background:linear-gradient(150deg,#c8b8a8,#8b93a0 50%,#4a5260 100%)" role="img" aria-label="Selfie of club members gathered beside a vehicle"></div>
  <h3>Kovo Officially Reveals the 2021 Production Strider Falcon 517!</h3>
  <div class="meta"><span><svg width="10" height="14" viewBox="0 0 10 14"><path d="M5 0a5 5 0 0 0-5 5c0 3.5 5 9 5 9s5-5.5 5-9a5 5 0 0 0-5-5zm0 7a2 2 0 1 1 0-4 2 2 0 0 1 0 4z" fill="#333"/></svg>UAE</span><span><svg width="12" height="12" viewBox="0 0 12 12"><rect x="0" y="2" width="12" height="10" fill="#333"/><rect x="2" y="0" width="2" height="3" fill="#333"/><rect x="8" y="0" width="2" height="3" fill="#333"/></svg>22.6.2023</span><span class="by"><svg width="12" height="12" viewBox="0 0 12 12"><circle cx="6" cy="3.5" r="3" fill="#d7323a"/><path d="M0 12c0-3.5 2.7-5 6-5s6 1.5 6 5z" fill="#d7323a"/></svg>by Tarek</span></div>
  <div class="tags"><span>Off-Road</span><span>Automotive</span><span>Club</span><span>Reviews</span></div>
</div>

<div class="abs card" style="top:2344px">
  <div class="pic" style="background:linear-gradient(160deg,#e2a35a,#d9a43c 50%,#6e5a30 100%)" role="img" aria-label="Front view of a yellow off-road vehicle on the dunes"></div>
  <h3>Kovo Officially Reveals the 2021 Production Strider Falcon 517!</h3>
  <div class="meta"><span><svg width="10" height="14" viewBox="0 0 10 14"><path d="M5 0a5 5 0 0 0-5 5c0 3.5 5 9 5 9s5-5.5 5-9a5 5 0 0 0-5-5zm0 7a2 2 0 1 1 0-4 2 2 0 0 1 0 4z" fill="#333"/></svg>UAE</span><span><svg width="12" height="12" viewBox="0 0 12 12"><rect x="0" y="2" width="12" height="10" fill="#333"/><rect x="2" y="0" width="2" height="3" fill="#333"/><rect x="8" y="0" width="2" height="3" fill="#333"/></svg>22.6.2023</span><span class="by"><svg width="12" height="12" viewBox="0 0 12 12"><circle cx="6" cy="3.5" r="3" fill="#d7323a"/><path d="M0 12c0-3.5 2.7-5 6-5s6 1.5 6 5z" fill="#d7323a"/></svg>by Tarek</span></div>
  <div class="tags"><span>Off-Road</span><span>Automotive</span><span>Club</span><span>Reviews</span></div>
</div>

<div class="abs card" style="top:2569px">
  <div class="pic" style="background:linear-gradient(180deg,#a9bccb,#c8d0d6 45%,#4d5358 70%,#9a9c9c 100%)" role="img" aria-label="Dark off-road vehicle on a road under a cloudy sky"></div>
  <h3>Kovo Officially Reveals the 2021 Production Strider Falcon 517!</h3>
  <div class="meta"><span><svg width="10" height="14" viewBox="0 0 10 14"><path d="M5 0a5 5 0 0 0-5 5c0 3.5 5 9 5 9s5-5.5 5-9a5 5 0 0 0-5-5zm0 7a2 2 0 1 1 0-4 2 2 0 0 1 0 4z" fill="#333"/></svg>UAE</span><span><svg width="12" height="12" viewBox="0 0 12 12"><rect x="0" y="2" width="12" height="10" fill="#333"/><rect x="2" y="0" width="2" height="3" fill="#333"/><rect x="8" y="0" width="2" height="3" fill="#333"/></svg>22.6.2023</span><span class="by"><svg width="12" height="12" viewBox="0 0 12 12"><circle cx="6" cy="3.5" r="3" fill="#d7323a"/><path d="M0 12c0-3.5 2.7-5 6-5s6 1.5 6 5z" fill="#d7323a"/></svg>by Tarek</span></div>
  <div class="tags"><span>Off-Road</span><span>Automotive</span><span>Club</span><span>Reviews</span></div>
</div>

<!-- our members -->
<div class="abs panel" style="left:773px;top:2077px;width:279px;height:400px"></div>
<h3 class="abs side-title" style="left:802px;top:2099px">Our Members</h3>
<div class="abs member" style="top:2147px"><div class="avatar" role="img" aria-label="Member avatar"></div><div style="width:122px"><b>Mateo Alvarez</b><small>on the trip</small></div><div class="dot"></div></div>
<div class="abs member" style="top:2224px"><div class="avatar" role="img" aria-label="Member avatar" style="background:linear-gradient(135deg,#6a7a8c,#2c3440)"></div><div style="width:122px"><b>Karim Haddad</b><small>on the trip</small></div><div class="dot"></div></div>
<div class="abs member" style="top:2301px"><div class="avatar" role="img" aria-label="Member avatar" style="background:linear-gradient(135deg,#b6cfe6,#c9a682)"></div><div style="width:122px"><b>Karim Haddad</b><small>on the trip</small></div><div class="dot"></div></div>
<div class="abs member" style="top:2377px"><div class="avatar" role="img" aria-label="Member avatar" style="background:linear-gradient(135deg,#8fa0b0,#3e3a3a)"></div><div style="width:122px"><b>Omar Selim</b><small>on the trip</small></div><div class="dot"></div></div>

<!-- newsletter -->
<svg class="abs newsletter" viewBox="0 0 1200 148" preserveAspectRatio="none">
  <rect width="1200" height="148" fill="#d7323a"/>
  <polygon points="0,0 549,0 496,148 0,148" fill="#2c2c2c"/>
</svg>
<h2 class="abs news-title">Subscribe Newsletter</h2>
<div class="abs email">Email:</div>
<a class="abs signup">SIGN UP</a>

<!-- footer -->
<div class="abs foot-brand"><i></i>DUNE CIRCLE</div>

<div class="abs foot-col" style="left:368px;top:3089px"><h4>Events</h4><ul><li>All Trips</li><li>Trips by levels</li><li>Trips Archive</li><li>Calendar View</li><li>Create Trip</li><li>Edit Trips</li><li>Manage Registrants</li></ul></div>
<div class="abs foot-col" style="left:556px;top:3089px"><h4>Links</h4><ul><li>Member trips</li><li>Sponsors</li><li>Dune Circle</li><li>Blog</li><li>E-Commerce</li><li>Contact Us</li></ul></div>
<div class="abs foot-col" style="left:712px;top:3089px"><h4>Forum</h4><ul><li>Your Posts</li><li>Board Index</li><li>New Posts</li><li>Unread Posts</li><li>Unanswered</li><li>Active Topics</li></ul></div>
<div class="abs foot-col" style="left:861px;top:3089px"><h4>Download<br>Membership Cards</h4></div>

<div class="abs tile" style="left:861px;top:3159px;background:#1c1c1e" role="img" aria-label="Add membership card to phone wallet"></div>
<div class="abs tile" style="left:949px;top:3159px;background:#3a7ee8" role="img" aria-label="Add membership card to phone wallet"></div>
<div class="abs social" style="left:866px;top:3247px" role="img" aria-label="Short video social profile"></div>
<div class="abs social" style="left:912px;top:3247px" role="img" aria-label="Photo social profile @dunecircle.ae"></div>

<div class="abs rule"></div>
<div class="abs copy">© 2023 Dubai, UAE. All rights are reserved.</div>

</body>
</html>
```